Business card to promote business guidance

I need a card design to give to all my customers advertising a way to build a business exactly like the one they just bought from. I have an online store and will include one with each shipment. It should state the way to financial freedom and working for yourself

Target Market(s)

Young Entrepreneurs that want to start and don't know how

Industry/Entity Type

Business

Contact Information for Business Card

"You just bought from a successful company on Brindlemart. I have a unique business model, discovered by me, unlike any other that can make anyone successful. Follow me and message me for exactly the same model. If you ever wanted to work for yourself, I will teach you how. It's not a pipe dream, allow me to guide you out of the box."

Colors
85abd2

Requirements
Must have
• website www.dorianwelkby.example
instagram @thedorianwelkby

```html
<!DOCTYPE html>
<html lang="en">
<head>
<meta charset="utf-8">
<title>Dorian Welkby – Business Card</title>
<link rel="stylesheet" href="https://fonts.googleapis.com/css2?family=Poppins:wght@300;400;600;700&display=swap">
<style>
  :root {
    --backdrop: #2a2a2a;
    --card: #ffffff;
    --accent: #85abd2;
    --card-shadow: rgba(0, 0, 0, 0.45);
  }
  * { margin: 0; padding: 0; box-sizing: border-box; }
  html, body {
    width: 1200px;
    height: 900px;
    overflow: hidden;
    background: var(--backdrop);
    font-family: "Poppins", sans-serif;
  }
  .canvas {
    width: 1200px;
    height: 900px;
    display: flex;
    flex-direction: column;
    align-items: center;
    justify-content: center;
    gap: 44px;
  }
  .card {
    position: relative;
    width: 630px;
    height: 360px;
    background: var(--card);
    box-shadow: 0 14px 34px var(--card-shadow);
    color: var(--accent);
  }

  /* Front side */
  .card-front .website {
    position: absolute;
    top: 128px;
    left: 0;
    right: 0;
    text-align: center;
    font-weight: 400;
    font-size: 25px;
    letter-spacing: 0.2em;
    text-transform: uppercase;
  }
  .card-front .social {
    position: absolute;
    left: 60px;
    bottom: 62px;
    display: flex;
    align-items: center;
    gap: 8px;
    font-weight: 300;
    font-size: 17px;
  }
  .social-dot {
    width: 16px;
    height: 16px;
    border: 2px solid var(--accent);
    border-radius: 50%;
  }

  /* Back side */
  .card-back .quote {
    position: absolute;
    top: 64px;
    left: 66px;
    right: 58px;
    font-weight: 400;
    font-size: 17.5px;
    line-height: 1.42;
  }
  .quote-mark {
    position: absolute;
    font-weight: 700;
    font-size: 62px;
    line-height: 1;
    letter-spacing: -0.06em;
  }
  .quote-mark.open { top: 38px; left: 34px; }
  .quote-mark.close { bottom: 8px; right: 46px; }
  .brand-name { font-weight: 600; }
</style>
</head>
<body>
  <main class="canvas">
    <section class="card card-front" aria-label="Card front">
      <p class="website">www.dorianwelkby.example</p>
      <p class="social"><span class="social-dot" aria-hidden="true"></span>@thedorianwelkby</p>
    </section>

    <section class="card card-back" aria-label="Card back">
      <span class="quote-mark open" aria-hidden="true">“</span>
      <p class="quote">You just bought from a successful company on <span class="brand-name">Brindlemart</span>. I have a unique business model, discovered by me, unlike any other that can make anyone successful. Follow me and message me for exactly the same model. If you ever wanted to work for yourself, I will teach you how. It’s not a pipe dream, allow me to guide you out of the box.</p>
      <span class="quote-mark close" aria-hidden="true">”</span>
    </section>
  </main>
</body>
</html>
```